Business Card Design Project

Hi,

We are a new modern sheet metal business and I require a business card for our sales reps.

The card should be double sided and standout in a crowd.

I have attached our logo and our website is www.folvik.com.au.

Please ask if you have any further questions
Updates

hi everyone, 

I'm wondering if we can try to lighten the cards mood.  Everyone is using black and I'm not sure how that would be accepted in real life.

Gregory

Reason: Still No receiving what I was hoping for.

Industry/Entity Type

Business

Requirements
Must have
• double sided

```html
<!DOCTYPE html>
<html lang="en">
<head>
<meta charset="utf-8">
<title>Folvik – Business Card</title>
<link rel="stylesheet" href="https://fonts.googleapis.com/css2?family=Source+Sans+3:wght@400;600;700&display=swap">
<style>
  :root {
    --navy: #243a7e;
    --navy-deep: #1f2a5e;
    --ink: #111111;
    --accent: #f39a2b;
    --white: #ffffff;
    --rule: #c6c6ca;
    --footer: #e3e7f0;
  }
  * { margin: 0; padding: 0; box-sizing: border-box; }
  html, body {
    width: 1200px; height: 613px; overflow: hidden;
    background: var(--white);
    font-family: "Source Sans 3", sans-serif;
  }
  .card { position: relative; width: 1200px; height: 613px; background: var(--white); }

  .header {
    position: absolute; left: 0; top: 0; width: 1200px; height: 211px;
    background: linear-gradient(90deg, var(--navy) 0%, var(--navy-deep) 100%);
  }
  .brand {
    position: absolute; left: 150px; top: 40px;
    color: var(--white); font-weight: 700; font-size: 112px;
    line-height: 1; letter-spacing: 2px;
  }
  .services {
    position: absolute; right: 79px; top: 30px;
    list-style: none; text-align: right;
    color: var(--white); font-weight: 400; font-size: 33px; line-height: 55px;
  }

  .person { position: absolute; right: 700px; top: 310px; text-align: right; }
  .person-name { color: var(--ink); font-weight: 700; font-size: 60px; line-height: 1; }
  .person-role { color: var(--navy); font-weight: 400; font-size: 32px; line-height: 1; margin-top: 10px; }

  .contacts { position: absolute; left: 708px; top: 279px; list-style: none; }
  .contacts li {
    display: flex; align-items: flex-start;
    color: var(--navy); font-size: 30px; line-height: 39px;
  }
  .contacts .icon { width: 28px; height: 28px; margin: 6px 26px 0 0; flex: none; }
  .contacts .no-icon { width: 28px; margin-right: 26px; flex: none; }

  .footer-rule { position: absolute; left: 0; top: 510px; width: 1200px; height: 9px; background: var(--rule); }
  .footer {
    position: absolute; left: 0; top: 519px; width: 1200px; height: 94px;
    background: var(--footer);
    display: flex; align-items: center; justify-content: center;
  }
  .website { color: var(--navy); font-weight: 700; font-size: 44px; letter-spacing: 1px; }
</style>
</head>
<body>
<div class="card">
  <header class="header">
    <div class="brand">FOLVIK</div>
    <ul class="services">
      <li>Flashings</li>
      <li>Gutter</li>
      <li>Rainwater Goods</li>
    </ul>
  </header>

  <section class="person">
    <h1 class="person-name">Daniel Hart</h1>
    <p class="person-role">sales manager</p>
  </section>

  <ul class="contacts">
    <li>
      <svg class="icon" viewBox="0 0 24 24" aria-hidden="true"><path fill="var(--accent)" d="M12 1.5a7.5 7.5 0 0 0-7.5 7.5c0 5.3 7.5 13.5 7.5 13.5s7.5-8.2 7.5-13.5A7.5 7.5 0 0 0 12 1.5zm0 10.2a2.7 2.7 0 1 1 0-5.4 2.7 2.7 0 0 1 0 5.4z"/></svg>
      <span>Address line 1</span>
    </li>
    <li><span class="no-icon"></span><span>address line 2</span></li>
    <li>
      <svg class="icon" viewBox="0 0 24 24" aria-hidden="true"><path fill="var(--accent)" d="M6.6 2.5l3 3.6-1.8 2.6c1.2 2.8 3.6 5.2 6.5 6.5l2.6-1.8 3.6 3-1.6 3.6c-8.4-.4-15.3-7.3-15.7-15.7z"/></svg>
      <span>+380 000 000 00</span>
    </li>
    <li>
      <svg class="icon" viewBox="0 0 24 24" aria-hidden="true"><path fill="var(--accent)" d="M1.5 5h21v14h-21zM3.5 6.8v1.1l8.5 6 8.5-6V6.8zm0 3.4v6.6l4.8-3.2zm17 0l-4.8 3.4 4.8 3.2z"/></svg>
      <span>daniel.hart@folvik.com.au</span>
    </li>
  </ul>

  <div class="footer-rule"></div>
  <footer class="footer">
    <span class="website">www.folvik.com.au</span>
  </footer>
</div>
</body>
</html>
```